Business Card for Fashion House

We need a business card design for our personalize fashion service for our customers. the business card should reflect reliability, luxury and creativity.
The brand Gravetto is extracted from "Graceful Vetto"; Gravetto provides fashion designs sprinkled with luxury and style tailored for our elite clients character profile.
Gravetto is created for those who embody class and elegance with a passion for style.
Target Market(s)
Affluent Customers
Industry/Entity Type
Fashion
Contact Information for Business Card
Rania Bou Khalil
Fashion Designer
Telephone: +971 5550123
Mobile +971 555987
Emal q@z.com
Website www.gravetto-example.com
Social Media Youtube g+ Facebook Instagram Pin /gravetto
Font styles to use
Other font styles liked:
- Audrey provided
Look and feel
Each slider illustrates characteristics of the customer's brand and the style your logo design should communicate.

```html
<!DOCTYPE html>
<html lang="en">
<head>
<meta charset="utf-8">
<title>Gravetto — Business Card</title>
<link rel="stylesheet" href="https://fonts.googleapis.com/css2?family=Marcellus&family=Cormorant+Garamond:wght@500&family=Roboto:wght@400&display=swap">
<style>
  :root {
    --backdrop: #d6d6d6;
    --ink: #262827;
    --paper: #ffffff;
    --silver-light: #f2f2f2;
    --silver-dark: #9a9a9a;
    --text-light: #f4f4f4;
    --text-dark: #262827;
  }
  * { margin: 0; padding: 0; box-sizing: border-box; }
  html, body {
    width: 1200px; height: 852px; overflow: hidden;
    background: var(--backdrop);
  }
  .stage {
    position: relative; width: 1200px; height: 852px;
    display: flex; align-items: center; justify-content: center; gap: 40px;
  }
  .card {
    position: relative; width: 520px; height: 298px;
    border-radius: 24px; overflow: hidden;
    box-shadow: 0 6px 18px rgba(0,0,0,0.18);
  }
  .card-front {
    background: var(--ink);
    display: flex; align-items: center; justify-content: center;
  }
  .brand-name {
    font-family: "Marcellus", serif;
    font-size: 26px; letter-spacing: 0.42em;
    color: var(--text-light);
    padding-left: 0.42em;
  }
  .card-back { background: var(--paper); }
  .card-back .panel-shape { position: absolute; inset: 0; }
  .card-back .brand-name {
    position: absolute; left: 20px; top: 132px; width: 230px;
    text-align: center; font-size: 22px; letter-spacing: 0.36em;
    color: var(--text-dark);
  }
  .identity {
    position: absolute; right: 26px; top: 30px; text-align: right;
    color: var(--text-light);
  }
  .identity .person-name {
    font-family: "Cormorant Garamond", serif; font-weight: 500;
    font-size: 24px; line-height: 1;
  }
  .identity .person-role {
    font-family: "Roboto", sans-serif; font-size: 10px; margin-top: 3px;
  }
  .contacts {
    position: absolute; right: 24px; top: 176px;
    list-style: none; text-align: right;
    font-family: "Roboto", sans-serif; font-size: 11.5px;
    color: var(--text-light); line-height: 16px;
  }
  .contacts li { display: flex; justify-content: flex-end; align-items: center; gap: 8px; }
  .contacts svg { width: 11px; height: 11px; flex: none; }
  .contacts .social-handle { padding-right: 19px; margin-top: 2px; }
</style>
</head>
<body>
<main class="stage">
  <section class="card card-front" aria-label="Card front">
    <div class="brand-name">GRAVETTO</div>
  </section>

  <section class="card card-back" aria-label="Card back">
    <svg class="panel-shape" viewBox="0 0 520 298" preserveAspectRatio="none" aria-hidden="true">
      <defs>
        <linearGradient id="silverEdge" x1="0" y1="0" x2="1" y2="1">
          <stop offset="0" stop-color="var(--silver-dark)"/>
          <stop offset="0.5" stop-color="var(--silver-light)"/>
          <stop offset="1" stop-color="var(--silver-dark)"/>
        </linearGradient>
      </defs>
      <path d="M182 0 C262 40 300 170 306 298 L520 298 L520 0 Z" fill="var(--ink)"/>
      <path d="M176 0 C256 40 294 170 300 298" fill="none" stroke="url(#silverEdge)" stroke-width="7"/>
    </svg>

    <div class="brand-name">GRAVETTO</div>

    <div class="identity">
      <div class="person-name">Rania Bou Khalil</div>
      <div class="person-role">Fashion Designer</div>
    </div>

    <ul class="contacts">
      <li>+971 5550123
        <svg viewBox="0 0 12 12" aria-hidden="true"><circle cx="6" cy="6" r="5.3" fill="none" stroke="currentColor" stroke-width="1"/><path d="M4 3.2l1 1.4-.6.7a4 4 0 0 0 2.3 2.3l.7-.6 1.4 1-.5 1c-2.6 0-4.8-2.2-4.8-4.8z" fill="currentColor"/></svg>
      </li>
      <li>+971 555987
        <svg viewBox="0 0 12 12" aria-hidden="true"><rect x="3" y="0.8" width="6" height="10.4" rx="1" fill="none" stroke="currentColor" stroke-width="1"/><circle cx="6" cy="9.4" r="0.6" fill="currentColor"/></svg>
      </li>
      <li>q@z.com
        <svg viewBox="0 0 12 12" aria-hidden="true"><rect x="0.8" y="2.3" width="10.4" height="7.4" fill="none" stroke="currentColor" stroke-width="1"/><path d="M0.8 2.3L6 6.6l5.2-4.3" fill="none" stroke="currentColor" stroke-width="1"/></svg>
      </li>
      <li>www.gravetto-example.com
        <svg viewBox="0 0 12 12" aria-hidden="true"><circle cx="6" cy="6" r="5.2" fill="none" stroke="currentColor" stroke-width="1"/><ellipse cx="6" cy="6" rx="2.2" ry="5.2" fill="none" stroke="currentColor" stroke-width="0.9"/><path d="M0.8 6h10.4M1.6 3.4h8.8M1.6 8.6h8.8" stroke="currentColor" stroke-width="0.8"/></svg>
      </li>
      <li class="social-handle">/gravetto</li>
    </ul>
  </section>
</main>
</body>
</html>
```